Eid Mubarak Digital Graphic

We seek designs for a digital greeting wishing our clients an Eid Mubarak. The graphic can contain Arabic and English text. This digital greeting should include our company logo.

Target Market(s)

Clients both commercial and government

Industry/Entity Type

Consulting

Font styles to use
Serif
Sans Serif
Decorative
Script
Other font styles liked:
• Arabic calligraphy

Requirements
Must have
• Digital graphic in a format easily sent by email and text
Company logo
Traditional Arabic greeting
Original graphic, not copied
Nice to have
• Arabic calligraphy
Should not have
• Nothing offensive to the Islamic religion

```html
<!DOCTYPE html>
<html lang="en">
<head>
<meta charset="utf-8">
<title>Eid Mubarak Greeting</title>
<link href="https://fonts.googleapis.com/css2?family=Amiri:wght@700&family=Caveat:wght@700&family=Montserrat:wght@600&family=Nunito:wght@600&display=swap" rel="stylesheet">
<style>
  :root {
    --night: #0c1e54;
    --gold: #f6c445;
    --white: #ffffff;
    --periwinkle: #7d9ef6;
    --brand-grey: #c9cdd8;
    --brand-orange: #f2812f;
    --hill-plum: #7b2f78;
    --hill-aqua: #6fdce6;
    --hill-teal: #1a9597;
    --drum-pink: #f4908f;
    --drum-yellow: #f6d45f;
    --figure-blue: #7b9cf5;
    --figure-purple: #7a2b73;
    --leaf-blue: #5f86f0;
  }
  html, body {
    margin: 0;
    padding: 0;
    overflow: hidden;
  }
  .greeting-card {
    position: relative;
    width: 1200px;
    height: 1200px;
    background: var(--night);
    overflow: hidden;
    font-family: "Nunito", sans-serif;
  }
  .brand {
    position: absolute;
    top: 72px;
    left: 0;
    width: 100%;
    display: flex;
    justify-content: center;
    align-items: center;
    gap: 18px;
  }
  .brand-name {
    font-family: "Nunito", sans-serif;
    font-weight: 600;
    font-size: 34px;
    letter-spacing: 2px;
    color: var(--brand-grey);
  }
  .brand-dot {
    width: 26px;
    height: 26px;
    border-radius: 50%;
    background: var(--brand-orange);
  }
  .arabic-greeting {
    position: absolute;
    top: 168px;
    left: 0;
    width: 100%;
    margin: 0;
    text-align: center;
    font-family: "Amiri", serif;
    font-weight: 700;
    font-size: 54px;
    line-height: 76px;
    color: var(--gold);
  }
  .headline {
    position: absolute;
    top: 236px;
    left: 0;
    width: 100%;
    margin: 0;
    text-align: center;
    font-family: "Caveat", cursive;
    font-weight: 700;
    font-size: 280px;
    line-height: 1;
    color: var(--gold);
  }
  .subhead {
    position: absolute;
    top: 520px;
    left: 0;
    width: 100%;
    margin: 0;
    text-align: center;
    font-family: "Montserrat", sans-serif;
    font-weight: 600;
    font-size: 46px;
    letter-spacing: 9px;
    color: var(--white);
  }
  .blessing {
    position: absolute;
    top: 634px;
    left: 0;
    width: 100%;
    margin: 0;
    text-align: center;
    font-weight: 600;
    font-size: 34px;
    line-height: 50px;
    color: var(--periwinkle);
  }
  .hills {
    position: absolute;
    left: 0;
    top: 0;
    width: 1200px;
    height: 1200px;
  }
  .illustration {
    position: absolute;
  }
  .illustration-leaves {
    left: 0;
    top: 975px;
    width: 265px;
    height: 225px;
    border-radius: 0 60% 0 0;
    background: linear-gradient(160deg, var(--leaf-blue), var(--hill-plum));
  }
  .illustration-drum {
    left: 245px;
    top: 850px;
    width: 305px;
    height: 272px;
    border-radius: 40px;
    background: linear-gradient(135deg, var(--drum-yellow), var(--drum-pink));
  }
  .illustration-figures {
    left: 728px;
    top: 800px;
    width: 300px;
    height: 340px;
    border-radius: 40px;
    background: linear-gradient(180deg, var(--figure-purple), var(--figure-blue));
  }
</style>
</head>
<body>
  <main class="greeting-card">
    <header class="brand">
      <span class="brand-name">MERIDIAN HARBOR ADVISORY LLC</span>
      <span class="brand-dot"></span>
    </header>

    <p class="arabic-greeting" lang="ar" dir="rtl">عيد مبارك</p>
    <h1 class="headline">Eid</h1>
    <p class="subhead">MUBARAK</p>
    <p class="blessing">
      May Allah provide you the strength<br>
      to be faithful to your fast and purposeful<br>
      with your prayers.
    </p>

    <svg class="hills" viewBox="0 0 1200 1200" aria-hidden="true">
      <path d="M0 1110 C120 1050 260 1030 380 1050 C500 1070 580 1130 630 1200 L0 1200 Z" fill="var(--hill-plum)"/>
      <path d="M1000 1070 C1080 1055 1150 1050 1200 1052 L1200 1200 L960 1200 Z" fill="var(--hill-teal)"/>
      <path d="M420 1200 C520 1090 640 1035 780 1035 C900 1035 990 1110 1020 1200 Z" fill="var(--hill-aqua)"/>
    </svg>

    <div class="illustration illustration-leaves" role="img" aria-label="Palm fronds and leaves at the bottom left"></div>
    <div class="illustration illustration-drum" role="img" aria-label="A traditional pink and yellow bedug drum resting on a wooden stand"></div>
    <div class="illustration illustration-figures" role="img" aria-label="A woman in hijab and a man in a kufi holding sparklers"></div>
  </main>
</body>
</html>
```